Indian Takeaway Menu -

I would like to have double parallel fold A4 sheet menu.
A4 sheet cut in half and attached to the other half to make the sheet 4 small pages long.

Colors
abd036
ffffff

Requirements
Must have
• Please check new attachments - menu size and layout is not correct.
• I would like to add Dark brown colour. A4 sheet folded 4x Menu layout pocket size.
Nice to have
• Dark Brown - Parrot Green and very light Brown

```html
<!DOCTYPE html>
<html lang="en">
<head>
<meta charset="utf-8">
<title>Saffron Lantern – Takeaway Menu</title>
<link href="https://fonts.googleapis.com/css2?family=Roboto+Condensed:wght@300;400;700&display=swap" rel="stylesheet">
<style>
:root{
  --green:#abd036;
  --green-soft:#f1f6dc;
  --brown:#2e1a12;
  --cream:#f6f6e6;
  --ink:#1d1d1b;
  --muted:#666;
  --red:#d9322b;
  --stage:#5f625a;
  --white:#ffffff;
}
*{margin:0;padding:0;box-sizing:border-box}
html,body{width:1200px;height:888px;overflow:hidden;background:var(--stage);font-family:"Roboto Condensed",Arial,sans-serif;color:var(--ink)}
.sheet{position:absolute;top:90px;width:453px;height:639px;background:var(--white);overflow:hidden}
.sheet--front{left:127px}
.sheet--back{left:605px}
.abs{position:absolute}
.brand{display:flex;align-items:center;gap:4px;font-weight:700;font-size:15px;color:var(--brown);white-space:nowrap}
.brand-mark{width:9px;height:9px;background:var(--green)}
.bar{background:var(--green);color:var(--brown);font-weight:700;display:flex;align-items:center;padding-left:6px}
.photo{border-radius:1px}
.item-name{display:flex;justify-content:space-between;font-size:9px;color:var(--ink)}
.item-name .flag{margin-left:4px}
.desc{font-size:5.4px;line-height:1.35;color:var(--muted);margin-top:2px;font-weight:300}
.side-item{width:152px;padding-bottom:6px;border-bottom:1px dotted #999}
.legend{border:1px solid var(--green);background:var(--green-soft);font-size:5.6px;line-height:1.7;padding:5px 8px;color:var(--ink)}
.deal-title{font-size:9px;font-weight:700}
.badge{width:15px;height:15px;border-radius:50%;background:var(--red);color:#fff;font-size:6px;font-weight:700;display:flex;align-items:center;justify-content:center}
.dash{border-bottom:1px dotted #999;width:126px}
.vdots{border-left:1px dotted #777}
.set-title{font-size:9px;font-weight:700}
.set-list{list-style:none;font-size:5.6px;line-height:11px;margin-top:4px}
.set-list li::before{content:"✓";color:var(--muted);margin-right:4px}
.foot{left:0;top:503px;width:453px;height:136px;background:var(--cream)}
.allergen{font-size:7.6px;line-height:16px}
.contact-h{font-size:11px;font-weight:700;display:flex;align-items:center;gap:4px}
.contact-t{font-size:7.6px;line-height:14px}
.pill{background:var(--brown);color:#fff;border-radius:14px;font-size:8.6px;display:flex;align-items:center;justify-content:center}
.url-tab{background:var(--white);border-radius:0 0 10px 10px;font-size:8.4px;display:flex;align-items:center;justify-content:center}
.starters{background:var(--green);color:var(--white)}
.starters h2{font-size:12px;font-weight:700;position:absolute;left:6px;top:6px}
.st-col{width:95px}
.st .item-name{color:var(--brown);font-size:6.8px}
.st .desc{color:#fff;font-size:4.6px;margin-top:1px;font-weight:400}
.st{position:absolute}
.sec-head{height:30px;overflow:hidden}
.sec-head .label{position:absolute;left:0;top:8px;background:rgba(46,26,18,.85);color:#fff;font-size:7px;padding:3px 6px 3px 8px}
.list{font-size:6.8px;list-style:none}
.list li{display:flex;height:15.5px;align-items:center}
.list .n{flex:1}
.list .c{width:50px}
.list .p{width:26px;text-align:right}
.curry{font-size:6.8px}
.curry .desc{font-size:4.4px;margin-top:1px}
.tint{background:var(--green-soft)}
.nan-box{border:4px solid var(--green);padding:8px 10px;background:#fff}
.nan-box h3{font-size:7.4px;font-weight:400;line-height:1.2}
.nan-list{list-style:none;font-size:4.8px;margin-top:6px;color:var(--muted)}
.nan-list li{display:flex;height:9.5px}
.nan-list .n{flex:1}
</style>
</head>
<body>

<!-- FRONT SHEET -->
<section class="sheet sheet--front">
  <div class="abs brand" style="left:14px;top:16px"><span class="brand-mark"></span>Saffron Lantern</div>

  <div class="abs bar" style="left:114px;top:14px;width:333px;height:18px;font-size:11px">Healthy&nbsp; Side orders</div>

  <div class="abs photo" role="img" aria-label="Photo of a pan of chicken curry on a rustic wooden table" style="left:6px;top:46px;width:98px;height:194px;background:linear-gradient(160deg,#c9c1b4,#c9582a 45%,#8c3b1c 70%,#b7ada0)"></div>

  <div class="abs side-item" style="left:120px;top:47px">
    <div class="item-name"><span>Sautéed Broccoli<span class="flag">v</span></span><span>5.00</span></div>
    <div class="desc">Broccoli, green beans and spinach leaves sautéed with roasted cumin and fresh garlic.</div>
  </div>
  <div class="abs side-item" style="left:120px;top:93px">
    <div class="item-name"><span>Chana Saag&nbsp; 3<span class="flag">y v</span></span><span>5.00</span></div>
    <div class="desc">Chickpeas cooked with chopped spinach, onion, and cumin and finished with cream.</div>
  </div>
  <div class="abs side-item" style="left:120px;top:139px">
    <div class="item-name"><span>Chana Masala<span class="flag">&nbsp; v</span></span><span>5.00</span></div>
    <div class="desc">Chickpeas simmered with tomato, caramelised onion, black pepper and fresh coriander.</div>
  </div>
  <div class="abs" style="left:120px;top:185px;width:152px">
    <div class="item-name"><span>Aloo Saag&nbsp; 3<span class="flag">y v</span></span><span>5.00</span></div>
    <div class="desc">Crispy Potato with spinach, caramelised onion, garam masala and a dash of cream.</div>
  </div>

  <div class="abs side-item" style="left:288px;top:47px">
    <div class="item-name"><span>Aloo Ghobhi<span class="flag">&nbsp; v</span></span><span>5.00</span></div>
    <div class="desc">Crispy Potatoes cubes &amp; Cauliflower cooked with roasted cumin with tomato and onion gravy.</div>
  </div>
  <div class="abs side-item" style="left:288px;top:93px">
    <div class="item-name"><span>Tarka Daal&nbsp; 4<span class="flag">y v</span></span><span>5.00</span></div>
    <div class="desc">Home style soaked yellow chana cooked with cumin &amp; garam masala</div>
  </div>
  <div class="abs side-item" style="left:288px;top:139px">
    <div class="item-name"><span>Tangy Aloo<span class="flag">&nbsp; v</span></span><span>5.00</span></div>
    <div class="desc">Crispy Potatoes cubes cooked with roasted cumin and touch of our tangy sauce</div>
  </div>
  <div class="abs legend" style="left:288px;top:177px;width:158px;height:31px">Y: can be cooked without allergen&nbsp; H: Healthy Option<br>V: Suitable for Vegans</div>

  <div class="abs bar" style="left:5px;top:252px;width:441px;height:18px;font-size:11px">Meal Deals only €8.50&nbsp;<span style="font-weight:400;font-size:7px">(Low Fat Dishes)</span></div>
  <div class="abs" style="left:13px;top:276px;font-size:6px">Choose with Rice or Plain Naan</div>

  <div class="abs photo" role="img" aria-label="Bowl of chicken dupiaza" style="left:13px;top:297px;width:44px;height:37px;background:linear-gradient(135deg,#e7e1d6,#c9642c 60%,#7c3a18)"></div>
  <div class="abs badge" style="left:49px;top:307px">8.5$</div>
  <div class="abs" style="left:66px;top:297px;width:126px"><div class="deal-title">Chicken Dupiaza</div><div class="desc">Chicken cooked with ginger and chunks of onions and finished with onion seeds</div></div>
  <div class="abs dash" style="left:66px;top:336px"></div>

  <div class="abs photo" role="img" aria-label="Dish of chicken rogan josh" style="left:13px;top:345px;width:44px;height:37px;background:linear-gradient(135deg,#d9d2c8,#a8391d 55%,#5a2010)"></div>
  <div class="abs badge" style="left:49px;top:355px">8.5$</div>
  <div class="abs" style="left:66px;top:346px;width:126px"><div class="deal-title">Chicken Rogan josh</div><div class="desc">A red chicken curry prepared with fresh herb &amp; spices, a delicacy from Kashmir</div></div>
  <div class="abs dash" style="left:66px;top:384px"></div>

  <div class="abs photo" role="img" aria-label="Plate of chicken bhuna" style="left:13px;top:393px;width:44px;height:37px;background:linear-gradient(135deg,#ece6da,#d26a2a 55%,#8a3c17)"></div>
  <div class="abs badge" style="left:49px;top:403px">8.5$</div>
  <div class="abs" style="left:66px;top:393px;width:126px"><div class="deal-title">Chicken Bhuna</div><div class="desc">Tomatoes and onion sauce cooked with black peppers &amp; spring onions</div></div>
  <div class="abs dash" style="left:66px;top:431px"></div>

  <div class="abs photo" role="img" aria-label="Bowl of tarkari makhani vegetables" style="left:13px;top:440px;width:44px;height:37px;background:linear-gradient(135deg,#e4ddcf,#e08a2c 55%,#9b4a16)"></div>
  <div class="abs badge" style="left:49px;top:450px">8.5$</div>
  <div class="abs" style="left:66px;top:440px;width:126px"><div class="deal-title">Tarkari Makhani</div><div class="desc">Mixed seasonal vegetables in a smooth tikka masala sauce</div></div>

  <div class="abs vdots" style="left:198px;top:296px;height:178px"></div>

  <div class="abs" style="left:214px;top:294px">
    <div class="set-title">Set Meal 1 ..........€16.00</div>
    <ul class="set-list"><li>Onion bhajia</li><li>Chicken Tikka Masala</li><li>Pilau rice</li><li>Naan</li><li>Poppadoms</li></ul>
  </div>
  <div class="abs" style="left:214px;top:379px">
    <div class="set-title">Set Meal 2 ..........€27.00</div>
    <ul class="set-list"><li>Onion bhajia</li><li>Chicken tikka</li><li>Chicken Tikka Masala</li><li>Lamb Roganjosh</li><li>2xPilau rice</li><li>1xNaan</li><li>Poppadom</li></ul>
  </div>
  <div class="abs vdots" style="left:327px;top:296px;height:100px"></div>
  <div class="abs" style="left:342px;top:294px">
    <div class="set-title">Set Meal 3/4 .........€43.00</div>
    <ul class="set-list"><li>Onion bhajia</li><li>Vegetable samosa</li><li>Chicken tikka</li><li>Chicken Tikka Masala</li><li>Lamb Roganjosh</li><li>Sambhar Veg Curry</li><li>2 x Pilau Rice</li><li>2 x Naan</li><li>Poppadom</li></ul>
  </div>
  <div class="abs" role="img" aria-label="Plate of grilled tandoori prawns and vegetables with a fork" style="left:333px;top:390px;width:120px;height:112px;background:radial-gradient(ellipse at 55% 55%,#e0763a 0%,#c55a2a 30%,#d9e2e6 62%,rgba(255,255,255,0) 75%)"></div>

  <div class="abs foot">
    <div class="abs allergen" style="left:26px;top:16px">1 celery ,<br>2 gluten ,<br>3 dairy ,<br>4 mustard,<br>5 nuts,</div>
    <div class="abs allergen" style="left:78px;top:16px">6 egg,<br>7 fish,<br>8 soya,<br>9 penuts,<br>10 lupin,</div>
    <div class="abs allergen" style="left:119px;top:16px">11 sulpher dioxide,<br>12 sesame seeds,<br>13 molluscs,<br>14 crustanceans</div>

    <div class="abs contact-h" style="left:215px;top:17px">
      <svg width="9" height="9" viewBox="0 0 24 24"><path fill="#1d1d1b" d="M6.6 10.8c1.4 2.8 3.8 5.1 6.6 6.6l2.2-2.2c.3-.3.7-.4 1-.2 1.1.4 2.3.6 3.6.6.6 0 1 .4 1 1V20c0 .6-.4 1-1 1C10.6 21 3 13.4 3 4c0-.6.4-1 1-1h3.5c.6 0 1 .4 1 1 0 1.3.2 2.5.6 3.6.1.3 0 .7-.2 1z"/></svg>PHONE</div>
    <div class="abs contact-t" style="left:227px;top:32px">+ 015550142,<br>+ 015550143</div>

    <div class="abs contact-h" style="left:290px;top:17px">
      <svg width="10" height="10" viewBox="0 0 24 24"><circle cx="12" cy="12" r="9" fill="none" stroke="#1d1d1b" stroke-width="2.4"/><path d="M12 7v5l3 2" fill="none" stroke="#1d1d1b" stroke-width="2.4"/></svg>OPENING HOURS:</div>
    <div class="abs contact-t" style="left:306px;top:32px">Sun - Thurs 5PM to 10.00PM<br>Fri &nbsp; - Sat &nbsp; 5.00PM-10.30PM</div>

    <div class="abs pill" style="left:215px;top:66px;width:135px;height:26px">Deliveries From 5.30PM</div>
    <div class="abs" style="left:358px;top:68px;font-size:8.6px;line-height:11px">All our meals are<br>cooked to order.</div>

    <div class="abs bar" style="left:6px;top:107px;width:440px;height:21px"></div>
    <div class="abs url-tab" style="left:159px;top:101px;width:130px;height:20px">www.saffronlantern.ie</div>
  </div>
</section>

<!-- BACK SHEET -->
<section class="sheet sheet--back">
  <div class="abs" role="img" aria-label="Photo of a bowl of yoghurt dessert topped with strawberries on a dark table" style="left:215px;top:7px;width:231px;height:232px;background:radial-gradient(circle at 62% 48%,#f4efe2 0%,#e8dcc0 32%,#6b5a50 55%,#2f2a2c 80%)"></div>
  <div class="abs starters" style="left:6px;top:7px;width:321px;height:232px">
    <h2>Starters</h2>
    <div class="st st-col" style="left:6px;top:32px"><div class="item-name"><span>Onion Bhajia</span><span>€4.50</span></div><div class="desc">Spinach &amp; onions fritters flavored with mild spices</div></div>
    <div class="st st-col" style="left:6px;top:67px"><div class="item-name"><span>Vegetable Samosa&nbsp; 2</span><span>€4.50</span></div><div class="desc">Crispy Pastry stuffed with potatoes, chick peas, Green peas mixed with desi spices until golden.</div></div>
    <div class="st st-col" style="left:6px;top:119px"><div class="item-name"><span>Palak Tikki</span><span>€ 4.50</span></div><div class="desc">Cakes of fresh spinach and chana dal</div></div>
    <div class="st st-col" style="left:6px;top:152px"><div class="item-name"><span>Veg Pakora</span><span>€ 5.00</span></div><div class="desc">Cauliflower, potato and broccoli, golden fried with Gram flour batter</div></div>
    <div class="st st-col" style="left:6px;top:190px"><div class="item-name"><span>Keema Singhara&nbsp; 2</span><span>€5.00</span></div><div class="desc">Spicy seasoned mince lamb in light pastry</div></div>

    <div class="st st-col" style="left:105px;top:32px"><div class="item-name"><span>Chicken Tikka&nbsp; 3</span><span>€5.00</span></div><div class="desc">Tender chicken marinated overnight with yoghurt, spices charred in tandoor</div></div>
    <div class="st st-col" style="left:105px;top:67px"><div class="item-name"><span>Seekh Kebab</span><span>€5.50</span></div><div class="desc">Skewered hand pounder lamb glazed in tandoor with green chilli &amp; black cardamom</div></div>
    <div class="st st-col" style="left:105px;top:108px"><div class="item-name"><span>Chicken Pakora</span><span>€ 5.00</span></div><div class="desc">Boneless pieces of chicken coated in gram flour batter with spices</div></div>
    <div class="st st-col" style="left:105px;top:141px"><div class="item-name"><span>Chicken Wings 2,1</span><span>€ 5.00</span></div></div>
    <div class="st st-col" style="left:105px;top:152px"><div class="item-name"><span>Tandoori Mix Meat<br>Platter&nbsp;&nbsp; 3</span><span>€9.50</span></div><div class="desc">Our special tandoori assortment of tandoori chicken on bone, seekh kebab and chicken tikka</div></div>
    <div class="st st-col" style="left:105px;top:202px"><div class="item-name"><span>Mix Veg platter 2</span><span>€9.50</span></div><div class="desc">Veg Samosa, Onion Bhaji, Veg Pakora</div></div>

    <div class="st st-col" style="left:209px;top:32px"><div class="item-name"><span>Doner Kebab 2,3,6</span><span>€8.00</span></div><div class="desc">Stripes of minced chicken &amp; beef served with garlic mayo, chilli sauce &amp; mixed salad &amp; wrapped in naan</div></div>
    <div class="st st-col" style="left:209px;top:75px"><div class="item-name"><span>Chicken Tikka<br>Kebab&nbsp;&nbsp; 2,3,6</span><span>€8.00</span></div><div class="desc">Chicken breast marinated in spices, barbecued served with garlic mayo, chilli sauce &amp; mixed salad &amp; wrapped in naan</div></div>
    <div class="st st-col" style="left:209px;top:130px"><div class="item-name"><span>Mix Kebab&nbsp; 2,3,6</span><span>€8.00</span></div><div class="desc">Pieces of chicken tikka &amp; doner meat with garlic mayo, sweet chilli &amp; salad wrapped in naan bread</div></div>
    <div class="st st-col" style="left:209px;top:173px"><div class="item-name"><span>Garlic Chips</span><span>€4.00</span></div></div>
  </div>

  <!-- section headers -->
  <div class="abs sec-head" role="img" aria-label="Banner photo of a curry dish" style="left:6px;top:252px;width:142px;background:linear-gradient(90deg,#e9e4dc,#c7582a 60%,#e9e4dc)"><span class="label">Chef Arun's Special Curries</span></div>
  <div class="abs sec-head" role="img" aria-label="Banner photo of grilled lamb" style="left:155px;top:252px;width:142px;background:linear-gradient(90deg,#3a2418,#8a4a25 50%,#4a2c1a)"><span class="label">Lamb Dishes</span></div>
  <div class="abs sec-head" role="img" aria-label="Banner photo of vegetable kebabs" style="left:305px;top:252px;width:142px;background:linear-gradient(90deg,#3a2a1c,#6f8a3a 50%,#5a3a20)"><span class="label">Vegetarian Dishes</span></div>

  <!-- chef curries -->
  <div class="abs curry" style="left:12px;top:290px;width:136px">
    <div class="item-name" style="font-size:6.8px"><span>Butter Murgh&nbsp; 3,5</span><span>€10.50</span></div>
    <div class="desc">Chicken cooked in tandoor mixed with rich tomato creamy cashew sauce, splash of cream with hint of honey &amp; dry fenugreek</div>
  </div>
  <div class="abs curry" style="left:12px;top:324px;width:136px">
    <div class="item-name" style="font-size:6.8px"><span>Laal Maas</span><span>€11.50</span></div>
    <div class="desc">Traditional rajasthani lamb cooked with garlic and ginger, ogel chilli powder, tomatoes finished with star aniseed and clove powder.</div>
  </div>
  <div class="abs curry" style="left:12px;top:362px;width:136px">
    <div class="item-name" style="font-size:6.8px"><span>Shahi Veg Kofta&nbsp;&nbsp; 3'5</span><span>€ 10.00</span></div>
    <div class="desc">Handmade veg and paneer dumplings simmered in tomato sauce, musky fenugreek sauce finished with touch of honey and cream</div>
  </div>
  <div class="abs curry" style="left:12px;top:399px;width:136px">
    <div class="item-name" style="font-size:6.8px"><span>Kerala Prawn&nbsp;&nbsp;&nbsp; 14</span><span>€ 12.00</span></div>
    <div class="desc">Delicacy of kerala spices, tomato and red onion gravy finished with touch of fresh coconut milk.</div>
  </div>
  <div class="abs curry" style="left:12px;top:436px;width:136px">
    <div class="item-name" style="font-size:6.8px"><span>Kerala Prawn&nbsp;&nbsp;&nbsp; 14</span><span>€ 12.00</span></div>
    <div class="desc">Delicacy of kerala spices, tomato and red onion gravy finished with touch of fresh coconut milk.</div>
  </div>

  <!-- lamb -->
  <div class="abs tint" style="left:155px;top:282px;width:142px;height:178px"></div>
  <ul class="abs list" style="left:163px;top:287px;width:128px">
    <li><span class="n">Punjabi Saag</span><span class="c">3 y</span><span class="p">9.95</span></li>
    <li><span class="n">Royale Korma</span><span class="c">3, 5</span><span class="p">€8.95</span></li>
    <li><span class="n">Saffron Lantern Chicken Curry 3,4,5</span><span class="p">€8.95</span></li>
    <li><span class="n">Chicken Karahi</span><span class="p">€8.95</span></li>
    <li><span class="n">Chicken Tikka Masala</span><span class="c">3</span><span class="p">€8.95</span></li>
    <li><span class="n">South Indian Garlic Chilli</span><span class="p">€8.95</span></li>
    <li><span class="n">Chicken Dahiwala</span><span class="c">3</span><span class="p">€8.95</span></li>
    <li><span class="n">Murgh Biryani&nbsp; 3,5,y</span><span class="p">€9.95</span></li>
    <li><span class="n">South Indian Garlic Chilli</span><span class="p">€8.95</span></li>
    <li><span class="n">Chicken Dahiwala</span><span class="c">3</span><span class="p">€8.95</span></li>
    <li><span class="n">Murgh Biryani&nbsp; 3,5,y</span><span class="p">€9.95</span></li>
  </ul>

  <!-- vegetarian -->
  <ul class="abs list" style="left:312px;top:287px;width:128px">
    <li><span class="n">Punjabi Saag</span><span class="c">3 y</span><span class="p">9.95</span></li>
    <li><span class="n">Royale Korma</span><span class="c">3, 5</span><span class="p">€8.95</span></li>
    <li><span class="n">Saffron Lantern Chicken Curry 3,4,5</span><span class="p">€8.95</span></li>
    <li><span class="n">Chicken Karahi</span><span class="p">€8.95</span></li>
    <li><span class="n">Chicken Tikka Masala</span><span class="c">3</span><span class="p">€8.95</span></li>
    <li><span class="n">South Indian Garlic Chilli</span><span class="p">€8.95</span></li>
    <li><span class="n">Chicken Dahiwala</span><span class="c">3</span><span class="p">€8.95</span></li>
  </ul>

  <div class="abs nan-box" style="left:313px;top:400px;width:134px;height:168px">
    <h3>Nan Bread &amp; Side Orders<br>All naan bread contains 2,3,6</h3>
    <ul class="nan-list">
      <li><span class="n">Naan.............................................</span><span>€2.20</span></li>
      <li><span class="n">Garlic Naan...................................</span><span>€2.50</span></li>
      <li><span class="n">Garlic Chilli Naan...........................</span><span>€3.00</span></li>
      <li><span class="n">Peshwari Naan..5..........................</span><span>€3.00</span></li>
      <li><span class="n">Keema Naan....................................</span><span>€3.00</span></li>
      <li><span class="n">Coriander Naan...............................</span><span>€2.50</span></li>
      <li><span class="n">Chilli Cheese Naan...3....................</span><span>€3.00</span></li>
      <li><span class="n">G.O.C.........................................</span><span>€3.00</span></li>
      <li><span class="n">Boiled Basmati.................................</span><span>€2.00</span></li>
      <li><span class="n">Pilau Rice........................................</span><span>€2.00</span></li>
      <li><span class="n">Lemon Rice...........4......................</span><span>€3.00</span></li>
      <li><span class="n">Poppodum(2)...................................</span><span>€2.50</span></li>
      <li><span class="n">Riata ...3.........................................</span><span>€2.50</span></li>
    </ul>
  </div>

  <!-- chicken & prawn -->
  <div class="abs sec-head" role="img" aria-label="Banner photo of chicken curry" style="left:6px;top:472px;width:142px;background:linear-gradient(90deg,#4a2a1a,#b04a22 50%,#6a3a20)"><span class="label">Chicken Dishes</span></div>
  <div class="abs sec-head" role="img" aria-label="Banner photo of prawn dish" style="left:155px;top:472px;width:142px;background:linear-gradient(90deg,#3a2a20,#d0703a 50%,#c8d0d2)"><span class="label">Prawn Dishes</span></div>
  <div class="abs tint" style="left:155px;top:502px;width:142px;height:130px"></div>

  <ul class="abs list" style="left:12px;top:504px;width:130px">
    <li><span class="n">Punjabi Saag</span><span class="c">3 y</span><span class="p">9.95</span></li>
    <li><span class="n">Royale Korma</span><span class="c">3, 5</span><span class="p">€8.95</span></li>
    <li><span class="n">Saffron Lantern Chicken Curry 3,4,5</span><span class="p">€8.95</span></li>
    <li><span class="n">Chicken Karahi</span><span class="p">€8.95</span></li>
    <li><span class="n">Chicken Tikka Masala</span><span class="c">3</span><span class="p">€8.95</span></li>
    <li><span class="n">South Indian Garlic Chilli</span><span class="p">€8.95</span></li>
    <li><span class="n">Chicken Dahiwala</span><span class="c">3</span><span class="p">€8.95</span></li>
    <li><span class="n">Murgh Biryani&nbsp; 3,5,y</span><span class="p">€9.95</span></li>
  </ul>
  <ul class="abs list" style="left:163px;top:504px;width:128px">
    <li><span class="n">Punjabi Saag</span><span class="c">3 y</span><span class="p">9.95</span></li>
    <li><span class="n">Royale Korma</span><span class="c">3, 5</span><span class="p">€8.95</span></li>
    <li><span class="n">Saffron Lantern Chicken Curry 3,4,5</span><span class="p">€8.95</span></li>
    <li><span class="n">Chicken Karahi</span><span class="p">€8.95</span></li>
    <li><span class="n">Chicken Tikka Masala</span><span class="c">3</span><span class="p">€8.95</span></li>
    <li><span class="n">South Indian Garlic Chilli</span><span class="p">€8.95</span></li>
    <li><span class="n">Chicken Dahiwala</span><span class="c">3</span><span class="p">€8.95</span></li>
    <li><span class="n">Murgh Biryani&nbsp; 3,5,y</span><span class="p">€9.95</span></li>
  </ul>

  <div class="abs brand" style="left:316px;top:590px;font-size:16px"><span class="brand-mark" style="width:10px;height:10px"></span>Saffron Lantern</div>
</section>

</body>
</html>
```